VoxMend needs a Letterhead

We need a letterhead for our company "VoxMend Consultants". Logo is attached. The company color is Turquoise. Icons for website, scan logo for website, icons for address, e-mail and phone appreciated rather than just words.

Industry/Entity Type

It Company

```html
<!DOCTYPE html>
<html lang="en">
<head>
<meta charset="utf-8">
<title>VoxMend Consultants – Letterhead</title>
<link rel="stylesheet" href="https://fonts.googleapis.com/css2?family=Jost:wght@400&display=swap">
<style>
  :root {
    --brand-deep: #0a8a93;
    --brand-turquoise: #30c9c0;
    --brand-tint: #e3f7f6;
    --paper: #ffffff;
  }
  html, body {
    margin: 0;
    padding: 0;
    overflow: hidden;
    background: var(--paper);
  }
  .letterhead {
    position: relative;
    width: 849px;
    height: 1200px;
    background: var(--paper);
    overflow: hidden;
    font-family: "Jost", "Futura", sans-serif;
    color: var(--brand-deep);
  }
  .stripes {
    position: absolute;
    left: 0;
    width: 130px;
  }
  .stripes--top { top: 0; height: 24px; }
  .stripes--side { top: 208px; height: 962px; }
  .stripe {
    position: absolute;
    top: 0;
    bottom: 0;
    width: 4px;
  }
  .stripe--deep { background: var(--brand-deep); }
  .stripe--light { background: var(--brand-turquoise); }

  .brand-name {
    position: absolute;
    left: 27px;
    top: 104px;
    margin: 0;
    font-size: 32px;
    font-weight: 400;
    line-height: 1;
    color: var(--brand-deep);
    white-space: nowrap;
  }

  .contact-list {
    position: absolute;
    right: 56px;
    top: 78px;
    margin: 0;
    padding: 0;
    list-style: none;
    text-align: right;
  }
  .contact-item {
    display: flex;
    justify-content: flex-end;
    align-items: center;
    gap: 9px;
    height: 22px;
    margin-bottom: 21.5px;
    font-size: 17px;
    letter-spacing: 0.3px;
    white-space: nowrap;
  }
  .contact-icon {
    width: 16px;
    height: 16px;
    flex: none;
    fill: var(--brand-turquoise);
  }

  .site-code {
    position: absolute;
    right: 56px;
    top: 1010px;
    width: 76px;
    height: 76px;
    background: var(--brand-tint);
    border: 2px solid var(--brand-turquoise);
    box-sizing: border-box;
  }

  .address {
    position: absolute;
    right: 53px;
    top: 1112px;
    display: flex;
    align-items: center;
    gap: 6px;
    font-size: 17.5px;
    font-style: normal;
    letter-spacing: 0.3px;
    white-space: nowrap;
  }
  .address-icon {
    width: 20px;
    height: 28px;
    fill: var(--brand-turquoise);
  }
</style>
</head>
<body>
<main class="letterhead">
  <div class="stripes stripes--top" aria-hidden="true">
    <span class="stripe stripe--deep" style="left:28px"></span>
    <span class="stripe stripe--deep" style="left:42px"></span>
    <span class="stripe stripe--deep" style="left:56px"></span>
    <span class="stripe stripe--deep" style="left:71px"></span>
    <span class="stripe stripe--light" style="left:88px"></span>
    <span class="stripe stripe--light" style="left:102px"></span>
    <span class="stripe stripe--light" style="left:116px"></span>
  </div>

  <h1 class="brand-name">VoxMend Consultants</h1>

  <ul class="contact-list">
    <li class="contact-item">
      <span>+ 91 9876501234</span>
      <svg class="contact-icon" viewBox="0 0 24 24" aria-hidden="true"><path d="M6.6 10.8a15.2 15.2 0 0 0 6.6 6.6l2.2-2.2a1 1 0 0 1 1-.25 11.4 11.4 0 0 0 3.6.57 1 1 0 0 1 1 1V20a1 1 0 0 1-1 1A17 17 0 0 1 3 4a1 1 0 0 1 1-1h3.5a1 1 0 0 1 1 1c0 1.25.2 2.45.57 3.6a1 1 0 0 1-.25 1z"/></svg>
    </li>
    <li class="contact-item">
      <span>hello@voxmend.com</span>
      <svg class="contact-icon" viewBox="0 0 24 24" aria-hidden="true"><path d="M2 6h20v12H2z"/><path d="M2 6l10 7 10-7" fill="none" stroke="#fff" stroke-width="1.6"/></svg>
    </li>
    <li class="contact-item">
      <span>www.voxmend.com</span>
      <svg class="contact-icon" viewBox="0 0 24 24" aria-hidden="true"><g fill="none" stroke="#30c9c0" stroke-width="1.6"><circle cx="12" cy="12" r="9.5"/><ellipse cx="12" cy="12" rx="4.5" ry="9.5"/><path d="M2.5 12h19M4 7h16M4 17h16"/></g></svg>
    </li>
  </ul>

  <div class="stripes stripes--side" aria-hidden="true">
    <span class="stripe stripe--deep" style="left:28px"></span>
    <span class="stripe stripe--deep" style="left:42px"></span>
    <span class="stripe stripe--deep" style="left:56px"></span>
    <span class="stripe stripe--deep" style="left:71px"></span>
    <span class="stripe stripe--light" style="left:88px"></span>
    <span class="stripe stripe--light" style="left:102px"></span>
    <span class="stripe stripe--light" style="left:116px"></span>
  </div>

  <div class="site-code" role="img" aria-label="Scannable code linking to www.voxmend.com"></div>

  <address class="address">
    <span>No.12/4, M 7th Cross, Bengaluru, KA - 560041.</span>
    <svg class="address-icon" viewBox="0 0 20 28" aria-hidden="true"><path d="M10 0a10 10 0 0 0-10 10c0 7 10 18 10 18s10-11 10-18A10 10 0 0 0 10 0zm0 14a4 4 0 1 1 0-8 4 4 0 0 1 0 8z"/></svg>
  </address>
</main>
</body>
</html>
```